Looking for a PowerPoint design for a Pharmaceutical Company

We need a PowerPoint template design to be used company-wide. We are a pharmaceutical company with 63 years of history and want to use a new template design to work more efficiently and effectively. Below are some of the things we are looking for in the new template design.

- Simple, modern, and professional

- Practical for every day use (easy to read, easy to create)

- Slides will be mainly projected or viewed on screens, but should also work fine when printed. (e.g. We do not want to use up our inks / toners printing several pages..)

- It would be great if you could provide us a list of colors that can be effectively used in the slides. (e.g. for highlighting fonts / multiple graph colors / etc.)

- Just as an FYI, our current logo image is (dark) blue. I am not uploading the logo image here because we do not want you to be limited by the current logo image. Depending on the design, we may / may not put our logo image on the slides.

Please feel free to reach out to me if you have any questions. I look forward to seeing your design. Thank you!

Target Market(s)

Pharmaceutical industry. (To be used internally and externally)

Industry/Entity Type

Pharmaceutical

Font styles to use
Sans Serif

Requirements
Must have
• Title slide, Subtitle slide, graphs, charts, tables, bullet points, and any other slide style components normally included.
Nice to have
• - As we are in the pharma industry, we want the slides to give credibility. But we do not want it look "old", "boring", or "typical". Feel free to use unique / fresh colors.
Should not have
• - TOO many colors
• - Please do not use the images on our website, which contain faces. (Any image with faces in it...) They are stock images we bought for the website, and we do not want the images on our slides. (e.g. image of running woman on the main page, image of a surgeon, image of kids playing soccer, etc.)
• - We are not looking for a design that is a modified version of our website design. We are looking for something new.

```html
<!DOCTYPE html>
<html lang="en">
<head>
<meta charset="utf-8">
<title>Executive Summary</title>
<link href="https://fonts.googleapis.com/css2?family=Roboto:wght@400;500;700&display=swap" rel="stylesheet">
<style>
  :root {
    --bg: #eeeeee;
    --title-blue: #1f4fa8;
    --heading-blue: #173a8a;
    --navy: #0c2f82;
    --royal: #1b4fa8;
    --slate: #8fa3a3;
    --charcoal: #3d3d3d;
    --dusk: #4a4f66;
    --graphite: #666666;
    --text: #333333;
    --rule: #555555;
    --footer: #3a3a3a;
    --white: #ffffff;
  }
  * { margin: 0; padding: 0; box-sizing: border-box; }
  html, body { width: 1200px; height: 900px; overflow: hidden; }
  body { background: var(--bg); font-family: 'Roboto', Arial, sans-serif; color: var(--text); }
  .slide { position: relative; width: 1200px; height: 900px; overflow: hidden; }
  .slide-title {
    position: absolute; left: 22px; top: 14px;
    font-size: 36px; font-weight: 700; color: var(--title-blue); letter-spacing: -0.5px;
  }
  .header-rule { position: absolute; left: 0; top: 79px; width: 1200px; height: 2px; background: var(--rule); }
  .header-notch { position: absolute; left: 0; top: 0; }
  .brand { position: absolute; right: 20px; top: 14px; text-align: right; }
  .brand-name { font-size: 26px; font-weight: 500; color: var(--heading-blue); letter-spacing: 0.5px; }
  .brand-tagline { font-size: 17px; font-weight: 400; color: var(--heading-blue); margin-top: 4px; }
  .cycle { position: absolute; left: 0; top: 0; }
  .point { position: absolute; width: 270px; }
  .point h2 { font-size: 24px; font-weight: 500; color: var(--heading-blue); margin-bottom: 4px; }
  .point p { font-size: 18px; line-height: 27px; }
  .point--right { text-align: right; }
  .point--split h2 { text-align: right; }
  .footer { position: absolute; left: 0; bottom: 0; width: 1200px; height: 36px; background: var(--footer); }
  .footer p { position: absolute; right: 10px; top: 7px; font-size: 18px; color: var(--white); }
</style>
</head>
<body>
<div class="slide">
  <h1 class="slide-title">EXECUTIVE SUMMARY</h1>
  <div class="header-rule"></div>
  <svg class="header-notch" width="80" height="100" viewBox="0 0 80 100">
    <polygon points="33,80 72,80 52,99" fill="var(--navy)"/>
  </svg>

  <div class="brand">
    <div class="brand-name">NOVELLA HEALTH</div>
    <div class="brand-tagline">Caring for every tomorrow</div>
  </div>

  <svg class="cycle" width="1200" height="900" viewBox="0 0 1200 900">
    <g transform="translate(604.5 447)">
      <path d="M-174.8,-208.4 A272,272 0 0 1 -23.7,-271 L-20.5,-234.1 A235,235 0 0 0 -151.1,-180 Z" fill="var(--navy)"/>
      <path d="M23.7,-271 A272,272 0 0 1 174.8,-208.4 L151.1,-180 A235,235 0 0 0 20.5,-234.1 Z" fill="var(--navy)"/>
      <path d="M208.4,-174.8 A272,272 0 0 1 271,-23.7 L234.1,-20.5 A235,235 0 0 0 180,-151.1 Z" fill="var(--navy)"/>
      <path d="M271,23.7 A272,272 0 0 1 208.4,174.8 L180,151.1 A235,235 0 0 0 234.1,20.5 Z" fill="var(--slate)"/>
      <path d="M174.8,208.4 A272,272 0 0 1 23.7,271 L20.5,234.1 A235,235 0 0 0 151.1,180 Z" fill="var(--charcoal)"/>
      <path d="M-23.7,271 A272,272 0 0 1 -174.8,208.4 L-151.1,180 A235,235 0 0 0 -20.5,234.1 Z" fill="var(--dusk)"/>
      <path d="M-208.4,174.8 A272,272 0 0 1 -271,23.7 L-234.1,20.5 A235,235 0 0 0 -180,151.1 Z" fill="var(--graphite)"/>
      <path d="M-271,-23.7 A272,272 0 0 1 -208.4,-174.8 L-180,-151.1 A235,235 0 0 0 -234.1,-20.5 Z" fill="var(--royal)"/>
    </g>
    <g fill="none" stroke-width="3">
      <polyline points="252,217 333,217 402,280" stroke="var(--royal)"/>
      <polyline points="772,242 835,178 960,178" stroke="var(--navy)"/>
      <polyline points="877,423 952,423" stroke="var(--navy)"/>
      <polyline points="252,472 372,472" stroke="var(--graphite)"/>
      <polyline points="315,717 372,717 440,660" stroke="var(--dusk)"/>
      <polyline points="783,600 862,680 960,680" stroke="var(--slate)"/>
    </g>
  </svg>

  <div class="point" style="left:64px; top:200px;">
    <h2>Heading Here</h2>
    <p>Subtext here Subtext here Sub-<br>text here Subtext here Subtext<br>here Subtext here</p>
  </div>
  <div class="point" style="left:64px; top:463px;">
    <h2>Heading Here</h2>
    <p>Subtext here Subtext here Sub-<br>text here Subtext here Subtext<br>here Subtext here</p>
  </div>
  <div class="point" style="left:66px; top:695px; width:200px;">
    <h2>Heading Here</h2>
    <p>Subtext here Subtext<br>here Subtext here Sub-<br>text here Subtext here<br>Subtext here</p>
  </div>
  <div class="point point--right" style="right:68px; top:163px;">
    <h2>Heading Here</h2>
    <p>Subtext here Subtext here Sub-<br>text here Subtext here Subtext<br>here Subtext here</p>
  </div>
  <div class="point point--right" style="right:53px; top:407px;">
    <h2>Heading Here</h2>
    <p>Subtext here Subtext here Sub-<br>text here Subtext here Subtext<br>here Subtext here</p>
  </div>
  <div class="point point--split" style="left:880px; top:667px;">
    <h2>Heading Here</h2>
    <p>Subtext here Subtext here Sub-<br>text here Subtext here Subtext<br>here Subtext here</p>
  </div>

  <div class="footer"><p>Copyright text here</p></div>
</div>
</body>
</html>
```